Used Car Business Card Design

Maple Ridge Auto Sales is a woman owned women friendly car lot.  We focus on providing Professionalism, Integrity and Respect beginning with the initial introduction.  We place the highest importance on customer service after the sale and our rating with the TVB of Arkansas shows it.  We're starting out 7th year, recently relocated. Satisfied Clients bring their family members, friends and co-workers to buy their cars, SUV's and trucks from MRAS.
You buy here / you pay here, Lending program opportunities too, Great Cash Prices
Finance with Flexibility we look at each individual uniquely and not a credit score
I think of my kids when getting our vehicles ready and your safety when you drive away in a MRAS car. . .  Drive away with Peace of Mind...
Maroon, Black and Silver colors.

Updates
I sent a response to the designers - have  not heard from them, will I receive my funds back?

Thank you all,  a lot of great designs - Making my decision on Nov 4th

So much talent. . .
So very challenging. . .
Thank you for your participation.
Sincerely,
Maple Ridge Auto Sales
Lorna Pickett

Industry/Entity Type
Safety
Contact Information for Business Card
Maple Ridge Auto Sales
"A Sound Car at a Fair Price"
4153 Garvey Rd. Cedar Bluff, Ar 72904
Lorna Pickett
501.389.7312

```html
<!DOCTYPE html>
<html lang="en">
<head>
<meta charset="utf-8">
<title>Maple Ridge Auto Sales – Business Card</title>
<link rel="stylesheet" href="https://fonts.googleapis.com/css2?family=Open+Sans:wght@300;400;800&display=swap">
<style>
  :root {
    --canvas: #cfd6d2;
    --card-black: #141416;
    --paper: #ffffff;
    --maroon: #3b1622;
    --ink: #1a1a1a;
    --silver-dark: #7f9192;
    --silver-mid: #aab6b7;
    --silver-light: #eef2f2;
    --gold: #b8935a;
    --copper: #7a4a2a;
    --soft-grey: #b9bcbc;
  }
  * { box-sizing: border-box; margin: 0; padding: 0; }
  html, body { width: 1200px; height: 1000px; overflow: hidden; }
  body {
    background: var(--canvas);
    font-family: "Open Sans", Arial, sans-serif;
    position: relative;
  }
  .card {
    position: absolute;
    left: 250px;
    width: 700px;
    height: 400px;
    background: var(--card-black);
    overflow: hidden;
    box-shadow: 0 10px 30px rgba(0,0,0,.25);
  }
  .card--front { top: 70px; }
  .card--back { top: 530px; }

  .silver-band {
    position: absolute;
    left: 0; right: 0;
    background: linear-gradient(100deg, var(--silver-mid) 0%, var(--silver-light) 28%, var(--silver-dark) 55%, var(--silver-light) 78%, var(--silver-mid) 100%);
    display: flex;
    align-items: center;
    justify-content: flex-end;
  }
  .silver-rule {
    position: absolute;
    left: 0; right: 0;
    height: 3px;
    background: linear-gradient(90deg, var(--silver-dark), var(--silver-light), var(--silver-dark));
  }
  .brand-name {
    font-weight: 800;
    color: var(--maroon);
    letter-spacing: -0.5px;
    white-space: nowrap;
  }
  .brand-sub {
    font-weight: 300;
    white-space: nowrap;
  }

  /* front */
  .card--front .silver-rule--top { top: 34px; }
  .card--front .silver-band { top: 46px; height: 112px; padding-right: 70px; }
  .card--front .silver-rule--bottom { top: 166px; }
  .card--front .brand-name { font-size: 60px; }
  .card--front .brand-sub {
    position: absolute;
    right: 70px;
    top: 178px;
    font-size: 30px;
    color: var(--soft-grey);
  }
  .tagline-strip {
    position: absolute;
    left: 0; right: 0; bottom: 0;
    height: 105px;
    background: var(--paper);
    display: flex;
    align-items: center;
    justify-content: center;
  }
  .tagline-strip::before {
    content: "";
    position: absolute;
    left: 0; right: 0; top: 0;
    height: 3px;
    background: linear-gradient(90deg, var(--copper), var(--gold) 40%, #e6d3a8 60%, var(--copper));
  }
  .tagline {
    font-size: 30px;
    font-weight: 400;
    color: var(--ink);
  }

  /* back */
  .card--back .silver-rule--top { top: 18px; }
  .card--back .silver-band { top: 28px; height: 80px; padding-right: 40px; gap: 12px; align-items: baseline; padding-top: 14px; }
  .card--back .silver-rule--bottom { top: 114px; }
  .card--back .brand-name { font-size: 44px; }
  .card--back .brand-sub { font-size: 28px; color: var(--paper); }
  .contact-panel {
    position: absolute;
    left: 0; right: 0;
    top: 124px;
    height: 220px;
    background: var(--paper);
    display: flex;
    flex-direction: column;
    justify-content: center;
    padding-left: 230px;
    line-height: 1.3;
  }
  .contact-name { font-size: 30px; color: var(--maroon); }
  .contact-line { font-size: 24px; color: var(--ink); }
  .back-tagline {
    position: absolute;
    left: 0; right: 0; bottom: 0;
    height: 56px;
    display: flex;
    align-items: center;
    justify-content: center;
    font-size: 22px;
    font-weight: 300;
    color: var(--soft-grey);
  }
</style>
</head>
<body>
  <section class="card card--front">
    <div class="silver-rule silver-rule--top"></div>
    <div class="silver-band"><span class="brand-name">Maple Ridge</span></div>
    <div class="silver-rule silver-rule--bottom"></div>
    <span class="brand-sub">Auto Sales</span>
    <div class="tagline-strip"><p class="tagline">- A Sound Car at a Fair Price -</p></div>
  </section>

  <section class="card card--back">
    <div class="silver-rule silver-rule--top"></div>
    <div class="silver-band"><span class="brand-name">Maple Ridge</span><span class="brand-sub">Auto Sales</span></div>
    <div class="silver-rule silver-rule--bottom"></div>
    <div class="contact-panel">
      <p class="contact-name">Lorna Pickett</p>
      <p class="contact-line">501.389.7312</p>
      <p class="contact-line">4153 Garvey Rd.</p>
      <p class="contact-line">Cedar Bluff, Ar 72904</p>
    </div>
    <p class="back-tagline">- A Sound Car at a Fair Price -</p>
  </section>
</body>
</html>
```